Lumivane, Business Intelligence Consultant Web Design

We need a web design for a Business Intelligence Consultant Enterprise.
We design, develop and mantain management systems and reports that delivered to the final user a complete information about their business. With that information they can take better management decisions.
Our principal service is KRV Business Intelligence proyects, using KRV Stockvault and KRV Quillmark tools.
Also we develop web systems that integrate mobile technology with KRV Systems and end user database systems.

Our principal objective is to be a partner of our clients more than a service provider, the idea is to offer a complete service to our customers that allow both companies grow togheter.

The final design must present our list of services and products, and show our experience in business intelligence projects.

Target Market(s)

Companies that runs KRV systems, Business companies, companies with production processes, retail, logistic process (inventory management)

Industry/Entity Type

Business

Requirements
Must have
• The brochure must have 4 pages:
Home
Empresa
Business Intelligence
Aplicaciones empresariales móviles
Metodología

And a contact form to receive customer contact.
- Name
- Company
- Contact Email
- Message text

For the color I will upload both company logos with different colors that u can use. Obviously you can add color if you want.
Nice to have
• The principal idea is to show to customer that all information of his business can be summarized on one graphic panel and can be consulted from any device.

Is nice to have business graphics on the web design, maybe abstract and give the idea of management information can be obtained easily.

Should not have
• Please, PLEASE!, don't use on the web site a meeting photo or people watching a business report on a lobby or some business man making a presentation.
Neither images of team building or people at the office.

That images are too used to present the business intelligence concept and the principal idea is to have information, and not people working hard to obtain that.

```html
<!DOCTYPE html>
<html lang="es">
<head>
<meta charset="utf-8">
<title>Lumivane — Business Intelligence</title>
<link rel="stylesheet" href="https://fonts.googleapis.com/css2?family=Carlito:wght@400;700&family=Montserrat:wght@300;400;500&family=PT+Sans:wght@400&family=Tinos&display=swap">
<style>
  :root {
    --header-black: #050505;
    --nav-top: #5c5c5e;
    --nav-bottom: #262628;
    --nav-divider: #1b1b1c;
    --accent-red: #d81f26;
    --page-grey: #5a5a60;
    --page-grey-dark: #4e4e53;
    --text-light: #e6e6e8;
    --text-muted: #b4b4b8;
    --title-box: #1f1f21;
    --newsletter-cyan: #2fbfd4;
    --newsletter-border: #66dcec;
    --subscribe-orange: #ee4a14;
    --footer-dark: #2b2b2d;
    --footer-line: #3f3f42;
    --footer-bottom: #333336;
    --white: #ffffff;
  }
  * { margin: 0; padding: 0; box-sizing: border-box; }
  html, body { width: 1089px; height: 1200px; overflow: hidden; }
  body {
    position: relative;
    background: var(--page-grey);
    font-family: "Montserrat", Arial, sans-serif;
    color: var(--text-light);
  }

  /* Header */
  .site-header {
    position: absolute; left: 0; top: 0; width: 1089px; height: 85px;
    background: var(--header-black);
  }
  .brand {
    position: absolute; left: 73px; top: 20px; height: 50px;
    display: flex; align-items: center; gap: 10px;
  }
  .brand-mark { width: 40px; height: 40px; background: #8a8a8e; }
  .brand-name {
    font-family: "Montserrat", Arial, sans-serif; font-weight: 400;
    font-size: 34px; color: var(--white); letter-spacing: -0.5px;
  }
  .header-call {
    position: absolute; right: 187px; top: 34px;
    font-size: 12.5px; color: #c8c8cc; font-weight: 400;
  }
  .header-call strong { color: var(--white); font-weight: 500; margin-left: 3px; }
  .header-social {
    position: absolute; left: 918px; top: 32px; display: flex; gap: 3px;
  }
  .header-social span { width: 22px; height: 22px; background: var(--white); border-radius: 2px; }

  /* Navigation */
  .main-nav {
    position: absolute; left: 0; top: 85px; width: 1089px; height: 40px;
    background: linear-gradient(var(--nav-top), var(--nav-bottom));
  }
  .main-nav ul { list-style: none; display: flex; position: absolute; left: 78px; top: 0; height: 40px; }
  .main-nav li {
    font-family: "PT Sans", Arial, sans-serif; font-size: 16px; color: var(--white);
    padding: 0 12px; line-height: 40px; border-right: 1px solid var(--nav-divider);
    text-transform: uppercase;
  }
  .main-nav li:last-child { border-right: none; }
  .main-nav li.is-active { background: linear-gradient(#e8323a, #b5141b); }
  .nav-shadow {
    position: absolute; left: 0; top: 125px; width: 1089px; height: 19px;
    background: linear-gradient(#1c1c1e, #3c3c40);
  }

  /* Content */
  .section-title {
    position: absolute; height: 44px;
    background: linear-gradient(#2c2c2e, #151516);
    border: 1px solid #6a6a6e; border-radius: 4px;
    box-shadow: 0 2px 4px rgba(0,0,0,0.4);
    font-family: "Carlito", Arial, sans-serif; font-size: 24px; color: var(--white);
    padding-left: 18px; line-height: 42px;
  }
  .title-main { left: 73px; top: 174px; width: 254px; }
  .title-side { left: 763px; top: 174px; width: 148px; padding-left: 10px; }

  .article-body {
    position: absolute; left: 73px; top: 238px; width: 625px;
    font-size: 12.2px; line-height: 19.3px; color: var(--text-light); font-weight: 400;
  }
  .article-body p { margin-bottom: 19.3px; }

  .column-divider {
    position: absolute; left: 733px; top: 160px; width: 3px; height: 600px;
    background: linear-gradient(var(--page-grey), #3e3e42 40%, var(--page-grey));
  }

  .testimonial { position: absolute; left: 763px; width: 256px; }
  .testimonial blockquote {
    font-size: 12.2px; line-height: 17.5px; color: var(--text-light); width: 240px;
  }
  .testimonial .role {
    text-align: right; font-size: 12.5px; color: var(--text-muted); margin-top: 14px;
  }
  .testimonial .person {
    text-align: right; font-family: "Carlito", Arial, sans-serif;
    font-size: 18px; color: var(--white); text-transform: uppercase; line-height: 18px;
  }

  /* Newsletter */
  .newsletter {
    position: absolute; left: 763px; top: 776px; width: 256px; height: 176px;
    background: var(--newsletter-cyan); border: 3px solid var(--newsletter-border);
    padding: 10px 14px;
  }
  .newsletter h3 {
    font-family: "Tinos", serif; font-weight: 400; font-size: 22px; color: var(--white);
  }
  .newsletter-icon {
    position: absolute; right: 20px; top: -3px; width: 36px; height: 34px;
    background: linear-gradient(#fafafa, #e5e5e5); border: 2px solid #e04a2a;
  }
  .newsletter p { font-family: Arial, sans-serif; font-size: 10.8px; line-height: 14px; color: var(--white); margin-top: 3px; }
  .newsletter label { display: block; font-family: Arial, sans-serif; font-size: 13px; color: var(--white); margin-top: 10px; }
  .newsletter .email-field { width: 222px; height: 27px; background: var(--white); margin-top: 2px; }
  .newsletter .subscribe {
    width: 224px; height: 28px; margin-top: 10px;
    background: linear-gradient(#f76a30, #d83a06);
    font-family: "Tinos", serif; font-size: 21px; color: var(--white);
    text-align: center; line-height: 28px;
  }

  /* Footer */
  .site-footer {
    position: absolute; left: 0; top: 1021px; width: 1089px; height: 140px;
    background: var(--footer-dark); border-top: 2px solid #202022;
  }
  .footer-heading { position: absolute; top: 26px; font-size: 15px; color: var(--white); font-weight: 400; }
  .footer-list { position: absolute; top: 62px; list-style: none; font-size: 12px; line-height: 17.5px; color: var(--text-muted); }
  .footer-email {
    position: absolute; left: 803px; top: 26px; font-size: 13px; color: var(--text-muted);
    display: flex;
  }
  .footer-email span:first-child { padding-right: 12px; border-right: 1px solid var(--footer-line); }
  .footer-email span:last-child { padding-left: 12px; }
  .footer-rule { position: absolute; left: 763px; width: 256px; height: 1px; background: var(--footer-line); }
  .stay-in-touch { position: absolute; left: 786px; top: 95px; font-size: 13px; color: var(--text-muted); }
  .footer-social { position: absolute; left: 925px; top: 84px; display: flex; gap: 4px; }
  .footer-social span { width: 32px; height: 32px; border-radius: 50%; background: #555558; border: 2px solid #3a3a3c; }

  .footer-bottom {
    position: absolute; left: 0; top: 1161px; width: 1089px; height: 39px;
    background: var(--footer-bottom); border-top: 1px solid #202022;
    font-size: 12px; color: var(--text-light); padding-left: 74px; line-height: 38px;
  }
</style>
</head>
<body>

<header class="site-header">
  <div class="brand">
    <span class="brand-mark"></span>
    <span class="brand-name">Lumivane</span>
  </div>
  <div class="header-call">For additional information call: <strong>+00 4821 3067</strong></div>
  <div class="header-social" aria-label="Social links">
    <span></span><span></span><span></span><span></span>
  </div>
</header>

<nav class="main-nav">
  <ul>
    <li>Home</li>
    <li>Empresa</li>
    <li class="is-active">Business Intelligence</li>
    <li>Aplicaciones empresariales móviles</li>
    <li>Metodología</li>
    <li>Contact us</li>
  </ul>
</nav>
<div class="nav-shadow"></div>

<h1 class="section-title title-main">Business Intelligence</h1>

<div class="article-body">
  <p>Lorem ipsum dolor sit amet, consectetur adipiscing elit. Suspendisse id lectus lorem, ut commodo tortor. Praesent nec suscipit quam. Sed mollis, velit at mattis mattis, felis elit cursus ipsum, et molestie diam erat ut massa. Nulla facilisi. Suspendisse vel massa vel dolor ultrices egestas. Vivamus viverra neque ac arcu consequat et adipiscing justo mattis. Sed quis magna at lacus auctor consectetur et ut justo. Vivamus a ante felis. Vestibulum ullamcorper, nisl eget ullamcorper vulputate, elit urna adipiscing magna, et vestibulum leo mauris dapibus tellus. Mauris at ipsum et ligula vestibulum sodales. Ut at tortor ipsum, in ultricies erat. Vestibulum sagittis ornare ligula et pellentesque. Aenean sed risus nulla, at adipiscing massa. In rutrum porta turpis. Maecenas dictum velit ut dui congue pulvinar. Sed dapibus odio sit amet lectus lobortis feugiat.</p>
  <p>Aliquam lacinia, nibh ut feugiat aliquam, mi ipsum faucibus nisl, ac egestas sapien tellus non massa. Suspendisse potenti. Etiam porta, ligula id eleifend vehicula, augue justo rhoncus nunc, aliquam volutpat nisi lorem nec orci. Integer et enim a dolor gravida suscipit nec sit amet justo. Fusce in sodales tortor. Sed ullamcorper orci neque. Mauris tincidunt, massa eu posuere faucibus, justo arcu pretium sem, in eleifend nisl sapien mollis ante. Phasellus leo leo, rhoncus vel fermentum et, aliquet ac mi. Duis vitae risus id metus imperdiet vulputate ut eget enim. Quisque adipiscing est sed metus aliquet varius. Ut tristique, urna a volutpat vestibulum, tortor erat accumsan est, sed rutrum lectus lorem id velit. Nullam lobortis, dui eu gravida laoreet, orci risus porta nibh, nec euismod nibh magna et justo. Proin nunc massa, volutpat eu malesuada et, lacinia porttitor nisi. Donec purus massa, porttitor at commodo et, tincidunt eget ligula.</p>
  <p>Ut nec purus eu ante blandit posuere consequat vel metus. Vivamus sagittis dignissim velit auctor varius. Nunc ullamcorper pretium facilisis. Cras bibendum pharetra mi, ut rhoncus lacus pretium vitae. Suspendisse sodales nisi lorem, ac mollis nisl. Sed ac lorem in magna auctor tincidunt. Vestibulum eget enim tortor. Nam ultrices vehicula diam, eget convallis metus pulvinar nec. Ut sed augue ac justo scelerisque tempus. Aliquam sem lorem, facilisis imperdiet hendrerit sed, congue quis turpis.</p>
</div>

<div class="column-divider"></div>

<h2 class="section-title title-side">Testimonials</h2>

<figure class="testimonial" style="top: 228px;">
  <blockquote>But I must explain to you how all this mistaken idea of denouncing pleasure and praising pain was born and I will give you a complete account of the system, and expound the actual teachings</blockquote>
  <figcaption><div class="role">Director</div><div class="person">Clara Voss</div></figcaption>
</figure>

<figure class="testimonial" style="top: 408px;">
  <blockquote>At vero eos et accusamus et iusto odio dignissimos ducimus qui blanditiis praesentium voluptatum deleniti atque corrupti quos dolores et quas molestias excepturi sint occaecati cupiditate non provident.</blockquote>
  <figcaption><div class="role">Senior assistant</div><div class="person">Tomas Reyl</div></figcaption>
</figure>

<figure class="testimonial" style="top: 588px;">
  <blockquote>But I must explain to you how all this mistaken idea of denouncing pleasure and praising pain was born and I will give you a complete account of the system, and expound the actual teachings</blockquote>
  <figcaption><div class="role">Junior researcher</div><div class="person">Aldo Petrane</div></figcaption>
</figure>

<section class="newsletter">
  <div class="newsletter-icon" role="img" aria-label="Envelope icon"></div>
  <h3>NEWSLETTER</h3>
  <p>Lorem ipsum dolor sit amet, consectetur adipisic ing elit, sed do eiusmod tempor.</p>
  <label>Email Address</label>
  <div class="email-field"></div>
  <div class="subscribe">SUBSCRIBE NOW</div>
</section>

<footer class="site-footer">
  <h4 class="footer-heading" style="left: 74px;">Contact Info</h4>
  <ul class="footer-list" style="left: 73px;">
    <li>123 Lorem ipsum dolor</li>
    <li>Some City, P.O 54898</li>
    <li>T: +00 4821 3090</li>
  </ul>
  <h4 class="footer-heading" style="left: 298px;">Quick Navigation</h4>
  <ul class="footer-list" style="left: 301px;">
    <li>Home</li>
    <li>Empresa</li>
    <li>Business Intelligence</li>
  </ul>
  <ul class="footer-list" style="left: 458px;">
    <li>Aplicaciones empresariales móviles</li>
    <li>Metodología</li>
    <li>Contact Us</li>
  </ul>
  <div class="footer-email"><span>EMAIL</span><span>Contact Us Now</span></div>
  <div class="footer-rule" style="top: 66px;"></div>
  <div class="stay-in-touch">STAY IN TOUCH</div>
  <div class="footer-social"><span></span><span></span></div>
  <div class="footer-rule" style="top: 119px;"></div>
</footer>

<div class="footer-bottom">© 2011 Lumivane. All right are reserved. &nbsp;Terms of service | Privacy Policy</div>

</body>
</html>
```